Business Card Design for an Investment Company

We need a business card design for our private investment company, called Ashbourne Partners. Ashbourne Partners is an investments partnership that aims to acquire shares in listed companies with a view to influencing those companies through active dialogue in order to improve their value. We need designs that use the logo colors (blue, grey, white), we need both English and Arabic on the business cards (can be on one side or 2 sides). The final logo should communicate professionalism, conservatism (nothing too fancy or too cheesy), that we are smart, conservative and old school.

Target Market(s)

Investment companies

Industry/Entity Type

Investment

Contact Information for Business Card

Khalid Yousef Rumaithi
Senior Executive Officer

Palm Terrace 07, Level 3, Office 215/12
HLMZ

+9714987650
krumaithi@ashbournepartners.com
www.ashbournepartners.com

Requirements
Must have
• Logo to be placed on the left hand side of the business card
• for the Arabic, we only need to have the name and title so it can be accomodated on one side so we can have the other side with full color and logo. The arabic that needs to be used is the below:
• خالد يوسف الرميثي
• المدير التنفيدي

```html
<!DOCTYPE html>
<html lang="en">
<head>
<meta charset="utf-8">
<title>Ashbourne Partners – Business Card</title>
<link rel="stylesheet" href="https://fonts.googleapis.com/css2?family=Lato:wght@400;700;900&family=Noto+Naskh+Arabic:wght@400;600&display=swap">
<style>
  :root{
    --blue:#1a8fc4;
    --blue-deep:#0f6fa3;
    --grey:#6b6b6b;
    --grey-text:#555;
    --band:#ececec;
    --paper:#f7f7f7;
    --stage:#e4e6e8;
  }
  *{box-sizing:border-box;margin:0;padding:0}
  html,body{width:1200px;height:780px;overflow:hidden}
  body{background:var(--stage);font-family:"Lato",sans-serif;position:relative}
  .card{position:absolute;top:110px;width:330px;height:560px;overflow:hidden;box-shadow:0 6px 18px rgba(0,0,0,.18)}
  .card--front{left:200px;background:var(--paper)}
  .card--back{left:670px;background:radial-gradient(circle at 50% 40%,#1d9fd4 0%,var(--blue) 45%,var(--blue-deep) 100%)}

  /* front */
  .edge-strip{position:absolute;left:0;top:0;width:18px;height:170px;background:var(--blue)}
  .edge-block{position:absolute;left:0;background:var(--blue)}
  .edge-block--mid{top:272px;width:56px;height:62px}
  .edge-block--foot{top:490px;width:52px;height:70px}
  .logo{position:absolute;left:36px;top:40px;display:flex;align-items:center;gap:8px;color:var(--blue);font-weight:900;font-size:19px;letter-spacing:.2px;white-space:nowrap}
  .logo__mark{width:12px;height:12px;background:var(--blue);flex:none}
  .name-bar{position:absolute;right:0;top:100px;width:220px;height:32px;background:var(--blue);color:#fff;font-weight:900;font-size:15px;display:flex;align-items:center;justify-content:flex-end;padding-right:20px;white-space:nowrap}
  .title{position:absolute;right:20px;top:140px;color:var(--grey-text);font-size:12px;letter-spacing:.4px}
  .contacts{position:absolute;left:0;width:330px}
  .contacts--en{top:180px}
  .contacts--ar{top:400px}
  .row{position:relative;height:28px;display:flex;align-items:center;padding-left:70px;font-size:11px;color:var(--grey-text);white-space:nowrap}
  .row::before{content:"";position:absolute;left:0;top:7px;width:46px;height:4px;background:var(--blue)}
  .row::after{content:"";position:absolute;left:58px;right:24px;bottom:0;height:6px;background:var(--band)}
  .row svg{position:absolute;left:50px;top:6px;width:12px;height:12px}
  .row--ar span{font-family:"Noto Naskh Arabic",serif;font-size:11px}
  .ar-bar{position:absolute;right:0;top:344px;width:220px;height:32px;background:var(--blue);color:#fff;font-family:"Noto Naskh Arabic",serif;font-weight:600;font-size:15px;line-height:1;display:flex;align-items:center;justify-content:flex-start;padding-right:20px;white-space:nowrap}
  .ar-title{position:absolute;right:20px;top:380px;font-family:"Noto Naskh Arabic",serif;font-size:12px;line-height:1.2;color:var(--grey-text)}

  /* back */
  .back-logo-band{position:absolute;left:0;right:0;top:200px;height:62px;background:#f2f2f2;display:flex;align-items:center;justify-content:flex-start;padding-left:30px;gap:8px;color:var(--blue);font-weight:900;font-size:20px;white-space:nowrap}
  .back-strip{position:absolute;left:0;right:0;height:16px;background:#eeeeee}
  .back-strip--upper{top:430px;left:40px;right:26px;opacity:.9}
  .back-info{position:absolute;left:0;right:0;top:460px;height:44px;background:#f2f2f2;display:flex;flex-direction:column;align-items:center;justify-content:center;gap:2px}
  .back-info__web{font-size:11px;color:var(--grey);letter-spacing:1.2px}
  .back-info__ar{font-family:"Noto Naskh Arabic",serif;font-size:10px;line-height:1.2;color:var(--grey)}
  .back-strip--lower{top:512px;left:34px;right:40px;background:#f2f2f2}
</style>
</head>
<body>

<section class="card card--front" aria-label="Card front">
  <div class="edge-strip"></div>
  <div class="edge-block edge-block--mid"></div>
  <div class="edge-block edge-block--foot"></div>

  <div class="logo"><span class="logo__mark"></span>Ashbourne Partners</div>

  <div class="name-bar">Khalid Yousef Rumaithi</div>
  <div class="title">Managing Director</div>

  <div class="contacts contacts--en">
    <div class="row">
      <svg viewBox="0 0 12 12"><rect width="12" height="12" fill="var(--blue)"/><path d="M3 4h6v1.5H7.5V7h1.5v1.5H3V7h1.5V5.5H3z" fill="#fff"/></svg>
      <span>+9714987650</span>
    </div>
    <div class="row">
      <svg viewBox="0 0 12 12"><rect width="12" height="12" fill="var(--blue)"/><rect x="2.5" y="3.5" width="7" height="5" fill="none" stroke="#fff"/><path d="M2.5 3.5L6 6.5 9.5 3.5" fill="none" stroke="#fff"/></svg>
      <span>krumaithi@ashbournepartners.com</span>
    </div>
    <div class="row">
      <svg viewBox="0 0 12 12"><rect width="12" height="12" fill="var(--blue)"/><circle cx="6" cy="6" r="3.5" fill="none" stroke="#fff"/><path d="M2.5 6h7M6 2.5v7" stroke="#fff"/></svg>
      <span>www.ashbournepartners.com</span>
    </div>
  </div>

  <div class="ar-bar" lang="ar" dir="rtl">خالد يوسف الرميثي</div>
  <div class="ar-title" lang="ar" dir="rtl">المدير التنفيدي</div>

  <div class="contacts contacts--ar">
    <div class="row">
      <svg viewBox="0 0 12 12"><rect width="12" height="12" fill="var(--blue)"/><path d="M3 4h6v1.5H7.5V7h1.5v1.5H3V7h1.5V5.5H3z" fill="#fff"/></svg>
      <span>+9714987650</span>
    </div>
    <div class="row row--ar">
      <svg viewBox="0 0 12 12"><rect width="12" height="12" fill="var(--blue)"/><rect x="2.5" y="3.5" width="7" height="5" fill="none" stroke="#fff"/><path d="M2.5 3.5L6 6.5 9.5 3.5" fill="none" stroke="#fff"/></svg>
      <span lang="ar" dir="rtl">قام تشكيل يعادل الإيطالية في</span>
    </div>
    <div class="row row--ar">
      <svg viewBox="0 0 12 12"><rect width="12" height="12" fill="var(--blue)"/><circle cx="6" cy="6" r="3.5" fill="none" stroke="#fff"/><path d="M2.5 6h7M6 2.5v7" stroke="#fff"/></svg>
      <span lang="ar" dir="rtl">قام تشكيل يعادل الإيطالية في</span>
    </div>
  </div>
</section>

<section class="card card--back" aria-label="Card back">
  <div class="back-logo-band"><span class="logo__mark"></span>Ashbourne Partners</div>
  <div class="back-strip back-strip--upper"></div>
  <div class="back-info">
    <span class="back-info__web">www.ashbournepartners.com</span>
    <span class="back-info__ar" lang="ar" dir="rtl">قام تشكيل يعادل الإيطالية في</span>
  </div>
  <div class="back-strip back-strip--lower"></div>
</section>

</body>
</html>
```